KTW Structural Approval Partners Certifiers

Professional Construction Consultancy Company Business Card - must keep logo colours see images below - examples have been added from my last competition - please see them as examples only!

Target Market(s)

Home Builders

Industry/Entity Type

Construction

Contact Information for Business Card

See "must haves"

Font styles to use
Sans Serif

Colors
ffffff
add136
000000

Requirements
Must have
• Daniel Moravec
• Director
• Phone: 0431 758 219
• Address: 17 Corrigan St,
• Holloway Vale, SA, 5098
• Email: ktwapprovalpartners@mailbox-example.com
• Website: www.ktwapprovalpartners.example.au
• Facebook: KTW Structural Approval Partners
Nice to have
• Side 1: full logo
• Side 2: company details
Should not have
• hard to read
• must be clear and professional

```html
<!DOCTYPE html>
<html lang="en">
<head>
<meta charset="utf-8">
<title>KTW Structural Approval Partners – Business Card</title>
<link rel="stylesheet" href="https://fonts.googleapis.com/css2?family=Montserrat:wght@400;500;700;800&display=swap">
<style>
  :root {
    --lime: #add136;
    --white: #ffffff;
    --black: #000000;
    --backdrop: #2b2b2b;
    --divider: #3a3a3a;
    --muted: #e6e6e6;
  }
  * { margin: 0; padding: 0; box-sizing: border-box; }
  html, body { width: 1200px; height: 900px; overflow: hidden; }
  body {
    background: var(--backdrop);
    font-family: "Montserrat", Arial, sans-serif;
    position: relative;
  }
  .card {
    position: absolute;
    width: 620px;
    height: 380px;
    background: var(--black);
    border-radius: 22px;
    box-shadow: 0 18px 40px rgba(0,0,0,.55);
    overflow: hidden;
  }
  /* Side 1 – full logo */
  .card-front { left: 120px; top: 50px; }
  .front-logo {
    position: absolute;
    left: 70px; top: 100px;
    color: var(--lime);
    font-weight: 800;
    display: flex;
    align-items: center;
    gap: 22px;
  }
  .front-logo .mark-square {
    width: 18px; height: 18px;
    background: var(--lime);
    flex: none;
  }
  .front-logo .logo-name {
    font-size: 34px;
    line-height: 1.05;
    letter-spacing: .5px;
    text-transform: uppercase;
  }
  .front-logo .logo-name span { display: block; }
  .front-logo .logo-name .initials { font-size: 72px; line-height: 1; letter-spacing: 0; }
  .front-web {
    position: absolute;
    right: 40px; bottom: 34px;
    color: var(--white);
    font-size: 17px;
    font-weight: 500;
  }
  .front-web .accent { color: var(--lime); }

  /* Side 2 – company details */
  .card-back { left: 460px; top: 470px; }
  .back-logo {
    position: absolute;
    left: 48px; top: 150px;
    display: flex; align-items: center; gap: 14px;
    color: var(--lime);
    font-weight: 800;
    font-size: 72px;
    line-height: 1;
  }
  .back-logo .mark-square { width: 16px; height: 16px; background: var(--lime); }
  .back-divider {
    position: absolute;
    left: 262px; top: 60px;
    width: 1px; height: 180px;
    background: var(--divider);
  }
  .details {
    position: absolute;
    left: 282px; top: 58px;
    color: var(--white);
    font-size: 14px;
    line-height: 1.55;
  }
  .details .person-name {
    color: var(--lime);
    font-weight: 700;
    font-size: 24px;
    text-transform: uppercase;
    line-height: 1.1;
  }
  .details .role { color: var(--muted); font-size: 15px; margin-bottom: 2px; }
  .details .address { margin-bottom: 6px; }
  .contact-list { list-style: none; font-size: 13px; }
  .contact-list li { display: flex; align-items: center; gap: 8px; }
  .contact-list svg { width: 12px; height: 12px; flex: none; }
  .contact-list .accent { color: var(--lime); font-weight: 700; }
  .social-dot { width: 10px; height: 10px; border-radius: 50%; background: var(--lime); flex: none; margin: 0 1px; }
</style>
</head>
<body>

<section class="card card-front" aria-label="Business card, front">
  <div class="front-logo">
    <div class="logo-name">
      <span class="initials">KTW</span>
      <span>Structural Approval</span>
      <span>Partners Certifiers</span>
    </div>
    <div class="mark-square"></div>
  </div>
  <p class="front-web">www.<span class="accent">ktwapprovalpartners</span>.example.au</p>
</section>

<section class="card card-back" aria-label="Business card, back">
  <div class="back-logo"><span>KTW</span><div class="mark-square"></div></div>
  <div class="back-divider"></div>
  <div class="details">
    <p class="person-name">Daniel Moravec</p>
    <p class="role">Director</p>
    <p class="address">17 Corrigan St,<br>Holloway Vale, SA, 5098</p>
    <ul class="contact-list">
      <li>
        <svg viewBox="0 0 24 24" aria-hidden="true"><path fill="#add136" d="M6.6 10.8a15 15 0 0 0 6.6 6.6l2.2-2.2c.3-.3.7-.4 1-.2 1.1.4 2.3.6 3.6.6.6 0 1 .4 1 1V20c0 .6-.4 1-1 1A17 17 0 0 1 3 4c0-.6.4-1 1-1h3.5c.6 0 1 .4 1 1 0 1.3.2 2.5.6 3.6.1.3 0 .7-.2 1z"/></svg>
        0431 758 219
      </li>
      <li>
        <svg viewBox="0 0 24 24" aria-hidden="true"><rect x="2" y="5" width="20" height="14" rx="2" fill="none" stroke="#add136" stroke-width="2"/><path d="M3 6l9 7 9-7" fill="none" stroke="#add136" stroke-width="2"/></svg>
        ktwapprovalpartners@mailbox-example.com
      </li>
      <li>
        <svg viewBox="0 0 24 24" aria-hidden="true"><circle cx="12" cy="12" r="9" fill="none" stroke="#add136" stroke-width="2"/><path d="M3 12h18M12 3c3 3 3 15 0 18M12 3c-3 3-3 15 0 18" fill="none" stroke="#add136" stroke-width="1.6"/></svg>
        <span>www.<span class="accent">ktwapprovalpartners</span>.example.au</span>
      </li>
      <li>
        <span class="social-dot" aria-hidden="true"></span>
        KTW Structural Approval Partners
      </li>
    </ul>
  </div>
</section>

</body>
</html>
```